Postcard Design Project

Company Name - Velmora Office Goods LLC We service and Repair printers, Fax and Copiers and sells all Business Technology supplies including supplies for Printers and Copiers to all NYC Metropolitan area.

Target Market(s)

NYC Small to Medium size business

Industry/Entity Type

Business

Font styles to use
Sans Serif

Colors

Designer to choose colors to be used in the design.

Requirements
Must have
• Printer Repairs and Toners Sales

```html
<!DOCTYPE html>
<html lang="en">
<head>
<meta charset="utf-8">
<title>Velmora Office Goods – Postcard</title>
<link rel="stylesheet" href="https://fonts.googleapis.com/css2?family=Oswald:wght@500;600&family=Open+Sans:wght@400;600;700&display=swap">
<style>
  :root{
    --page:#e4e4e4;
    --white:#ffffff;
    --ink:#1d1d1d;
    --cyan:#1ea3dc;
    --blue:#0c6db3;
    --navy:#0a4a86;
    --dark:#151515;
    --yellow:#ffe600;
    --lime:#a9cc2f;
    --green:#6cbf3a;
  }
  *{margin:0;padding:0;box-sizing:border-box}
  html,body{width:958px;height:1200px;overflow:hidden;background:var(--page)}
  body{position:relative;font-family:"Open Sans",Arial,sans-serif;color:var(--white)}
  .postcard{position:absolute;left:126px;width:706px;height:478px;overflow:hidden;background:var(--white)}
  .postcard--front{top:75px}
  .postcard--back{top:617px}
  .postcard__art{position:absolute;inset:0}
  .abs{position:absolute;white-space:nowrap}
  .brand{display:flex;align-items:center;gap:12px;color:var(--ink);font-weight:700}
  .brand__mark{background:var(--cyan);flex:none}
  .headline{font-family:"Oswald",Arial,sans-serif;font-weight:500;font-size:33px;letter-spacing:.3px;line-height:1}
  .tagline{font-size:15px;color:var(--yellow);font-weight:600}
  .section-label{font-family:"Oswald",Arial,sans-serif;font-weight:500;font-size:18px;color:var(--cyan);letter-spacing:.2px}
  .section-label .chev{margin-right:10px;font-weight:600}
  .body-copy{font-size:15px;line-height:24px}
  .highlight{color:var(--yellow)}
  .call{font-family:"Oswald",Arial,sans-serif;font-weight:500;font-size:28px;color:var(--yellow);display:flex;align-items:center;gap:10px}
  .call svg{width:24px;height:24px}
  .web{font-weight:700;font-size:15px;letter-spacing:.4px}
  .guarantee{font-family:"Oswald",Arial,sans-serif;font-weight:500;font-size:14.5px;color:var(--lime);line-height:20px;text-align:center}
  .benefits{list-style:none;font-size:15px;line-height:24px}
  .benefits li{display:flex;align-items:center;gap:8px}
  .benefits svg{width:12px;height:12px;flex:none}
  .signup{font-weight:700;font-size:12px}
</style>
</head>
<body>

<!-- Front side -->
<section class="postcard postcard--front">
  <svg class="postcard__art" width="706" height="478" viewBox="0 0 706 478">
    <defs>
      <linearGradient id="bandBlue" x1="0" y1="0" x2="1" y2="1">
        <stop offset="0" stop-color="#29aee6"/><stop offset="1" stop-color="#0a68ad"/>
      </linearGradient>
      <radialGradient id="darkPanel" cx="0.45" cy="0.3" r="0.8">
        <stop offset="0" stop-color="#4a4a4a"/><stop offset="1" stop-color="#0e0e0e"/>
      </radialGradient>
      <linearGradient id="ringGlow" x1="0" y1="0" x2="0" y2="1">
        <stop offset="0" stop-color="#f6d23b"/><stop offset=".55" stop-color="#f28b1c"/><stop offset="1" stop-color="#1ea3dc"/>
      </linearGradient>
      <radialGradient id="serviceTones" cx=".5" cy=".45" r=".6">
        <stop offset="0" stop-color="#e3e1dc"/><stop offset=".7" stop-color="#b9b6b0"/><stop offset="1" stop-color="#7e7a74"/>
      </radialGradient>
    </defs>
    <polygon points="590,0 706,0 706,478 470,478" fill="url(#bandBlue)"/>
    <polygon points="0,159 470,159 455,277 0,277" fill="url(#bandBlue)"/>
    <polygon points="0,277 470,277 455,478 0,478" fill="url(#darkPanel)"/>
    <circle cx="535" cy="238" r="192" fill="none" stroke="var(--cyan)" stroke-width="5"/>
    <circle cx="535" cy="238" r="181" fill="none" stroke="url(#ringGlow)" stroke-width="13"/>
    <g role="img" aria-label="Photo of a technician repairing an office laser printer">
      <circle cx="535" cy="238" r="171" fill="url(#serviceTones)"/>
    </g>
  </svg>

  <div class="abs brand" style="left:32px;top:58px;font-size:26px">
    <span class="brand__mark" style="width:30px;height:30px"></span>Velmora Office Goods
  </div>

  <h1 class="abs headline" style="left:32px;top:186px">GOT DIRTY PRINTER?</h1>
  <p class="abs tagline" style="left:32px;top:233px">Get a Tehnician in your office today!</p>

  <p class="abs section-label" style="left:32px;top:290px"><span class="chev">»</span>SERVICE CONTRACTS AVAILABLE</p>
  <p class="abs body-copy" style="left:32px;top:327px">Repairing of all kinds of Laser printers,<br>Fax &amp; Copiers, Paper Jams, Fuser Errors,<br>Paper crimping, Cleaning and much more...</p>

  <p class="abs call" style="left:32px;top:425px">CALL TODAY!
    <svg viewBox="0 0 24 24" aria-hidden="true"><circle cx="12" cy="12" r="10.5" fill="none" stroke="var(--yellow)" stroke-width="2"/><path d="M8.6 6.8l1.7 2.6-1 1.2c.7 1.6 1.9 2.8 3.5 3.5l1.2-1 2.6 1.7-.9 1.8c-3.9.2-8-3.9-7.8-7.8z" fill="var(--yellow)"/></svg>
    718 555 0142</p>

  <p class="abs web" style="left:510px;top:441px">www.velmoragoods.com</p>
</section>

<!-- Back side -->
<section class="postcard postcard--back">
  <svg class="postcard__art" width="706" height="478" viewBox="0 0 706 478">
    <defs>
      <linearGradient id="backBlue" x1="0" y1="0" x2="1" y2="1">
        <stop offset="0" stop-color="#2fb1e8"/><stop offset="1" stop-color="#0a5ea6"/>
      </linearGradient>
      <radialGradient id="backDark" cx=".35" cy=".3" r=".8">
        <stop offset="0" stop-color="#4a4a4a"/><stop offset="1" stop-color="#0f0f0f"/>
      </radialGradient>
      <linearGradient id="backRing" x1="1" y1="0" x2="0" y2="1">
        <stop offset="0" stop-color="#f6d23b"/><stop offset=".5" stop-color="#f28b1c"/><stop offset="1" stop-color="#1ea3dc"/>
      </linearGradient>
      <radialGradient id="printerTones" cx=".5" cy=".5" r=".6">
        <stop offset="0" stop-color="#f4f4f4"/><stop offset=".6" stop-color="#c9c9c9"/><stop offset="1" stop-color="#8a8a8a"/>
      </radialGradient>
    </defs>
    <polygon points="0,0 428,0 392,478 0,478" fill="url(#backBlue)"/>
    <polygon points="0,0 428,0 413,203 0,203" fill="url(#backDark)"/>
    <polygon points="0,395 402,395 396,442 0,442" fill="var(--dark)"/>
    <polygon points="0,442 395,442 392,478 0,478" fill="var(--navy)"/>
    <circle cx="425" cy="282" r="92" fill="none" stroke="url(#backRing)" stroke-width="8"/>
    <circle cx="425" cy="282" r="84" fill="var(--white)"/>
    <g role="img" aria-label="Photo of an inkjet printer printing a colour page">
      <circle cx="425" cy="282" r="78" fill="url(#printerTones)"/>
    </g>
    <rect x="593" y="23" width="96" height="63" fill="none" stroke="#9a9a9a" stroke-width="1.5"/>
    <circle cx="45" cy="238" r="22" fill="var(--green)" stroke="var(--white)" stroke-width="3"/>
  </svg>

  <div class="abs brand" style="left:432px;top:50px;font-size:11.5px;gap:6px">
    <span class="brand__mark" style="width:14px;height:14px"></span>Velmora Office Goods
  </div>

  <h2 class="abs headline" style="left:30px;top:30px">GOT DIRTY PRINTER?</h2>
  <p class="abs body-copy" style="left:30px;top:86px"><span class="highlight">SAVE ON</span> all your supplies like Toners, Drums,<br>Fuser and Maintenance kits.<br>Instant Discount and monthly rebats.</p>
  <p class="abs section-label" style="left:30px;top:167px"><span class="chev">»</span>SERVICE CONTRACTS AVAILABLE</p>

  <p class="abs guarantee" style="left:148px;top:217px">100% GUARANTEED<br>5 YEARS WARRANTY</p>

  <ul class="abs benefits" style="left:30px;top:284px">
    <li><svg viewBox="0 0 12 12" aria-hidden="true"><circle cx="6" cy="6" r="5.2" fill="none" stroke="var(--lime)" stroke-width="1.3"/><path d="M3.5 6.2l1.7 1.6 3.3-3.4" fill="none" stroke="var(--lime)" stroke-width="1.3"/></svg>Cost 30%-40% cheaper than OEM</li>
    <li><svg viewBox="0 0 12 12" aria-hidden="true"><circle cx="6" cy="6" r="5.2" fill="none" stroke="var(--lime)" stroke-width="1.3"/><path d="M3.5 6.2l1.7 1.6 3.3-3.4" fill="none" stroke="var(--lime)" stroke-width="1.3"/></svg>Oem Print Quality</li>
    <li><svg viewBox="0 0 12 12" aria-hidden="true"><circle cx="6" cy="6" r="5.2" fill="none" stroke="var(--lime)" stroke-width="1.3"/><path d="M3.5 6.2l1.7 1.6 3.3-3.4" fill="none" stroke="var(--lime)" stroke-width="1.3"/></svg>Print morepage yield then OEM</li>
    <li><svg viewBox="0 0 12 12" aria-hidden="true"><circle cx="6" cy="6" r="5.2" fill="none" stroke="var(--lime)" stroke-width="1.3"/><path d="M3.5 6.2l1.7 1.6 3.3-3.4" fill="none" stroke="var(--lime)" stroke-width="1.3"/></svg>4 Years more warranty than OEM</li>
  </ul>

  <p class="abs call" style="left:26px;top:398px">CALL TODAY!
    <svg viewBox="0 0 24 24" aria-hidden="true"><circle cx="12" cy="12" r="10.5" fill="none" stroke="var(--yellow)" stroke-width="2"/><path d="M8.6 6.8l1.7 2.6-1 1.2c.7 1.6 1.9 2.8 3.5 3.5l1.2-1 2.6 1.7-.9 1.8c-3.9.2-8-3.9-7.8-7.8z" fill="var(--yellow)"/></svg>
    718 555 0142</p>

  <p class="abs signup" style="left:30px;top:452px">Create an acount onlyne at: www.velmoragoods.com</p>
</section>

</body>
</html>
```